delivery service for warm food for kids and other kids stuff

plumwicks.nl > daycare website

plumwicks.shop >>> cartloom site we ask you to design!

We are a daycare center and thanks to corona found that we could help parents and kids while at home ! we would like some help to get an awesome and clear site for this.

it doesnt have to look kiddy...
more proffessional and sleek
we love quince website... so anything in that direction would be great!... ie pic next to text...
2 tone colors
ours are pink light blue and white.. so play with that?
black and white also fine!

Target Market(s)

expats and proffesional parents ... so NOT KIDDY website...

Font styles to use
Sans Serif

Requirements
Must have
• sexy design....
simplicity...
less text... more pictures
cool headlines
Should not have
• lots of text everyhwere
busy

```html
<!DOCTYPE html>
<html lang="en">
<head>
<meta charset="utf-8">
<title>Plumwicks Shop</title>
<link href="https://fonts.googleapis.com/css2?family=Titillium+Web:wght@400;600;700&family=Open+Sans:ital,wght@0,400;0,600;1,400&display=swap" rel="stylesheet">
<style>
:root{
  --ink:#3a3a5a;
  --muted:#9a9aa8;
  --pink:#e8578a;
  --blush:#e8b4c6;
  --sky:#cfe8f6;
  --cream:#f2ece0;
  --sand:#f3e5da;
  --blue:#2ea3f2;
  --yellow:#f7c81e;
  --grey:#efeff1;
  --line:#dcdce2;
  --footer:#282a38;
  --white:#fff;
}
*{box-sizing:border-box;margin:0;padding:0}
html,body{width:1200px;height:3236px;overflow:hidden}
body{position:relative;background:var(--white);color:var(--ink);font-family:"Open Sans",sans-serif;font-size:12px}
.abs{position:absolute}
h1,h2,h3,.brand{font-family:"Titillium Web",sans-serif}
.photo{position:absolute}

/* top bar */
.topbar{left:40px;top:0;width:1120px;height:63px;border-bottom:2px solid var(--line);display:flex;align-items:center;justify-content:space-between}
.gift{display:flex;align-items:center;gap:8px;font-size:16px;font-family:"Titillium Web",sans-serif;font-weight:600;position:relative}
.gift .badge{position:absolute;left:14px;top:-10px;background:var(--pink);color:#fff;font-size:10px;width:20px;height:20px;border-radius:50%;display:flex;align-items:center;justify-content:center}
.toplinks{display:flex;gap:20px;font-size:14px;font-weight:600}
.toplinks span+span{border-left:1px solid var(--line);padding-left:20px}

/* header */
.contact-chip{display:flex;align-items:center;gap:12px;font-size:9px;line-height:13px}
.contact-chip .ic{width:34px;height:34px;border-radius:50%;background:var(--grey);display:flex;align-items:center;justify-content:center}
.contact-chip em{font-style:normal;color:var(--blue)}
.search{left:812px;top:100px;width:204px;height:46px;border-radius:23px;background:var(--grey);display:flex;align-items:center;justify-content:space-between;padding:0 20px;font-size:13px}
.cart{left:1042px;top:101px;display:flex;align-items:center;gap:12px;font-family:"Titillium Web",sans-serif;font-weight:600;font-size:15px}
.cart .ic{width:44px;height:44px;border-radius:50%;background:var(--yellow);display:flex;align-items:center;justify-content:center}
.nav{left:0;top:171px;width:1200px;height:51px;background:var(--grey)}
.nav a{position:absolute;top:16px;font-size:14px;color:var(--ink);text-decoration:none;font-weight:600}
.logo-disc{left:530px;top:72px;width:152px;height:152px;border-radius:50%;background:var(--white);border:5px solid var(--blue);display:flex;align-items:center;justify-content:center;text-align:center}
.brand{font-weight:700;color:var(--pink);line-height:1}

/* hero */
.hero{left:40px;top:246px;width:1120px;height:482px;background:var(--pink);overflow:hidden}
.hero .disc{left:142px;top:83px;width:136px;height:136px;border-radius:50%;background:var(--white);border:4px solid var(--blue);display:flex;align-items:center;justify-content:center;text-align:center}
.hero h1{left:144px;top:240px;font-size:56px;color:var(--white);font-weight:700}
.hero p{left:148px;top:324px;font-size:17px;line-height:22px;color:var(--white)}
.arrow-btn{width:42px;height:42px;border-radius:50%;background:var(--white);display:flex;align-items:center;justify-content:center}
.dots{left:496px;top:440px;display:flex;gap:18px}
.dots i{width:12px;height:12px;border-radius:50%;border:1.5px solid var(--white)}
.dots i:first-child{background:var(--white)}

/* section heads */
.sec-title{font-size:36px;font-weight:600;color:var(--ink)}
.all-link{font-size:12px;font-weight:600;display:flex;align-items:center;gap:6px}
.all-link i{width:14px;height:14px;border-radius:50%;background:var(--ink)}
.round{width:36px;height:36px;border-radius:50%;background:var(--grey);display:flex;align-items:center;justify-content:center}
.round.light{background:var(--white)}

/* products */
.product .name{font-size:12px;margin-top:28px}
.stars{color:var(--yellow);font-size:9px;letter-spacing:1px}
.stars em{color:var(--muted);font-size:10px;margin-left:14px;letter-spacing:0}
.price{font-size:17px;margin-top:4px}
.price s{color:var(--muted);font-size:12px;margin-left:8px;text-decoration:none}

/* testimonial */
.quote{font-size:11px;font-style:italic;color:var(--muted);line-height:16px;width:325px}

/* blogs */
.blog h3{font-size:17px;font-weight:600}
.meta{display:flex;gap:60px;font-size:11px;font-style:italic;color:var(--muted);margin:10px 0;align-items:center}
.meta span{display:flex;align-items:center;gap:8px}
.avatar{width:22px;height:22px;border-radius:50%;background:#4f5580;display:inline-block}
.blog p{font-size:12px;line-height:17px;width:250px}
.blog .stats{font-size:10px;font-style:italic;color:var(--muted);margin-top:12px;display:flex;gap:30px}

/* newsletter */
.subscribe{left:609px;top:2628px;width:386px;height:38px;border:2px solid var(--line);border-radius:19px;display:flex;align-items:center;justify-content:space-between;padding-left:16px;font-size:13px;color:#c4c4cc}
.subscribe b{background:#4a4d72;color:#fff;height:38px;margin-right:-2px;padding:0 28px;border-radius:19px;display:flex;align-items:center;font-size:14px;font-weight:600}

/* footer */
.footer{left:0;top:2768px;width:1200px;height:468px;background:var(--footer);color:#c7c8d4}
.footer h3{position:absolute;top:80px;color:#fff;font-size:20px;font-weight:700;letter-spacing:.5px}
.footer .small{font-size:12px}
.social{display:flex;align-items:center;gap:16px;font-size:12px;margin-bottom:23px}
.social i{width:24px;height:24px;background:#fff;border-radius:3px;display:block}
.social i.c{border-radius:50%}
.cline{display:flex;gap:10px;font-size:12px;line-height:20px}
.cline a{color:var(--blue);text-decoration:none}
.f-input{border:1px solid #5a5c6e;height:34px;width:240px;font-size:12px;padding:9px;color:#7d7f90}
.f-btn{background:#4a4d6a;color:#fff;height:34px;width:240px;display:flex;align-items:center;justify-content:center;font-size:13px;font-weight:600}
</style>
</head>
<body>

<!-- top bar -->
<div class="abs topbar">
  <div class="gift">
    <svg width="22" height="22" viewBox="0 0 22 22"><rect x="2" y="8" width="18" height="13" fill="#3a3a5a"/><rect x="1" y="5" width="20" height="4" fill="#3a3a5a"/><rect x="10" y="5" width="2" height="16" fill="#fff"/></svg>
    <span class="badge">02</span>
    Gift Vouchers
  </div>
  <div class="toplinks"><span>ENG ⌄</span><span>USD ⌄</span><span>Sign in / Register</span></div>
</div>

<!-- header -->
<div class="abs contact-chip" style="left:56px;top:108px">
  <span class="ic"><svg width="14" height="14" viewBox="0 0 24 24"><path d="M6 2l4 4-2 3c1 3 4 6 7 7l3-2 4 4-3 4C10 22 2 14 2 5z" fill="#3a3a5a"/></svg></span>
  <span>Have any Questions?<br>Call: <em>0755 010 101</em></span>
</div>
<div class="abs contact-chip" style="left:262px;top:108px">
  <span class="ic"><svg width="12" height="14" viewBox="0 0 12 14"><path d="M1 0h10v14l-5-4-5 4z" fill="#3a3a5a"/></svg></span>
  <span>Discounts<br>Discounts <em style="color:var(--yellow)">up to 50%</em></span>
</div>
<div class="abs search">Search...
  <svg width="15" height="15" viewBox="0 0 16 16"><circle cx="6.5" cy="6.5" r="5" fill="none" stroke="#3a3a5a" stroke-width="1.8"/><path d="M10.5 10.5l4 4" stroke="#3a3a5a" stroke-width="1.8"/></svg>
</div>
<div class="abs cart">
  <span class="ic"><svg width="18" height="18" viewBox="0 0 18 18"><path d="M3 6h12l-1 10H4z" fill="#fff"/><path d="M6 6V4a3 3 0 016 0v2" fill="none" stroke="#fff" stroke-width="1.6"/></svg></span>
  My Cart
</div>

<nav class="abs nav">
  <a style="left:98px">Home</a>
  <a style="left:196px">Warm Food</a>
  <a style="left:327px">Flowers</a>
  <a style="left:435px">Drinks</a>
  <a style="left:724px">Healthy bars</a>
  <a style="left:864px">Puzzel mats</a>
  <a style="left:1002px">Courses</a>
</nav>
<div class="abs logo-disc"><span class="brand" style="font-size:26px">Plumwicks<br>Shop</span></div>

<!-- hero -->
<section class="abs hero">
  <div class="photo" role="img" aria-label="Smiling toddler in a yellow paper crown biting a blue spoon" style="left:560px;top:0;width:560px;height:482px;background:radial-gradient(ellipse at 60% 45%,#f1c9a8 0%,#e9a88c 30%,#e8578a 70%)"></div>
  <div class="abs disc"><span class="brand" style="font-size:24px">Plumwicks<br>Shop</span></div>
  <h1 class="abs">Plumwicks Kids Shop</h1>
  <p class="abs">We have partnered with our favorite companies<br>to bring you the best content and food</p>
  <div class="abs arrow-btn" style="left:24px;top:218px"><svg width="12" height="14"><path d="M8 2L3 7l5 5" fill="none" stroke="#3a3a5a" stroke-width="2"/></svg></div>
  <div class="abs arrow-btn" style="left:1054px;top:218px"><svg width="12" height="14"><path d="M4 2l5 5-5 5" fill="none" stroke="#3a3a5a" stroke-width="2"/></svg></div>
  <div class="abs dots"><i></i><i></i><i></i></div>
</section>

<!-- promo tiles -->
<div class="photo" role="img" aria-label="Toddler in a knit hat and yellow coat on pink" style="left:40px;top:776px;width:355px;height:212px;background:linear-gradient(90deg,#e8b4c6 40%,#c9a489 60%,#e8b4c6 75%)"></div>
<div class="photo" role="img" aria-label="Blonde girl portrait on cream" style="left:425px;top:776px;width:355px;height:212px;background:linear-gradient(90deg,#f2ece0 55%,#e2d2bd 70%,#f2ece0 85%)"></div>
<div class="photo" role="img" aria-label="Boy in navy cardigan and blue shorts on light blue" style="left:807px;top:776px;width:356px;height:212px;background:linear-gradient(90deg,#cfe8f6 60%,#5570a8 78%,#cfe8f6 95%)"></div>

<!-- featured -->
<h2 class="abs sec-title" style="left:40px;top:1056px">Featured Products</h2>
<div class="abs all-link" style="left:915px;top:1068px">All Products <i></i></div>
<div class="abs round" style="left:1064px;top:1058px"><svg width="10" height="12"><path d="M7 1L2 6l5 5" fill="none" stroke="#3a3a5a" stroke-width="2"/></svg></div>
<div class="abs round" style="left:1106px;top:1058px"><svg width="10" height="12"><path d="M3 1l5 5-5 5" fill="none" stroke="#3a3a5a" stroke-width="2"/></svg></div>

<div class="abs product" style="left:40px;top:1148px;width:188px">
  <div role="img" aria-label="Hand holding an ice cream cone" style="height:188px;background:linear-gradient(135deg,#c79a6e,#f0d7b4 50%,#8a5a3c)"></div>
  <div class="name">Product 01</div><div class="stars">★★★★★<em>6 Review(s)</em></div><div class="price">$36.00<s>$42.00</s></div>
</div>
<div class="abs product" style="left:267px;top:1148px;width:188px">
  <div role="img" aria-label="Glass of iced cola on orange" style="height:188px;background:radial-gradient(circle at 55% 60%,#5a2a16 0%,#8c4a1c 25%,#d8902e 55%)"></div>
  <div class="name">Product 02</div><div class="stars">★★★★★<em>6 Review(s)</em></div><div class="price">$36.00<s>$42.00</s></div>
</div>
<div class="abs product" style="left:493px;top:1148px;width:188px">
  <div role="img" aria-label="Blue plate with a lollipop on pink" style="height:188px;background:radial-gradient(circle at 50% 50%,#8fc8d8 0%,#8fc8d8 22%,#f7b6b8 30%)"></div>
  <div class="name">Product 03</div><div class="stars">★★★★★<em>6 Review(s)</em></div><div class="price">$36.00<s>$42.00</s></div>
</div>
<div class="abs product" style="left:720px;top:1148px;width:188px">
  <div role="img" aria-label="White bottle and orange slices on green" style="height:188px;background:linear-gradient(180deg,#0f5a45 0%,#0f6a50 60%,#12a07a 100%)"></div>
  <div class="name">Product 04</div><div class="stars">★★★★★<em>6 Review(s)</em></div><div class="price">$36.00<s>$42.00</s></div>
</div>
<div class="abs product" style="left:946px;top:1148px;width:188px">
  <div role="img" aria-label="Pink grapes on pink" style="height:188px;background:radial-gradient(circle at 50% 45%,#d8407a 0%,#e07aa0 25%,#ef94b3 45%)"></div>
  <div class="name">Product 05</div><div class="stars">★★★★★<em>6 Review(s)</em></div><div class="price">$36.00<s>$42.00</s></div>
</div>

<!-- banners -->
<div class="photo" role="img" aria-label="Two kids in colourful jackets looking at a phone" style="left:40px;top:1474px;width:725px;height:112px;background:linear-gradient(90deg,#f2ece0 60%,#c8467a 72%,#b89470 85%,#f2ece0 100%)"></div>
<div class="photo" role="img" aria-label="Toddler in a white t-shirt and dark jeans" style="left:792px;top:1474px;width:368px;height:112px;background:linear-gradient(90deg,#f3e5da 70%,#d8d8d8 82%,#3a3a44 90%,#f3e5da 100%)"></div>

<!-- latest -->
<h2 class="abs sec-title" style="left:40px;top:1654px">Latest Products</h2>
<div class="abs all-link" style="left:537px;top:1668px">All Products <i></i></div>
<div class="abs round light" style="left:686px;top:1658px"><svg width="10" height="12"><path d="M7 1L2 6l5 5" fill="none" stroke="#3a3a5a" stroke-width="2"/></svg></div>
<div class="abs round light" style="left:728px;top:1658px"><svg width="10" height="12"><path d="M3 1l5 5-5 5" fill="none" stroke="#3a3a5a" stroke-width="2"/></svg></div>

<div class="photo" role="img" aria-label="Macarons and tea on a white table" style="left:40px;top:1745px;width:112px;height:112px;background:linear-gradient(135deg,#e9e4d6,#b9c7a4 50%,#f3e0d0)"></div>
<div class="abs" style="left:173px;top:1743px"><div>Product 01</div><div class="stars" style="margin-top:4px">★★★★★<em>6 Review(s)</em></div><div class="price">$36.00<s>$42.00</s></div></div>
<div class="photo" role="img" aria-label="Bowls of spices and nuts" style="left:417px;top:1745px;width:112px;height:112px;background:linear-gradient(135deg,#d9d4cc,#8c5a3e 50%,#efe9e2)"></div>
<div class="abs" style="left:552px;top:1743px"><div>Product 01</div><div class="stars" style="margin-top:4px">★★★★★<em>6 Review(s)</em></div><div class="price">$36.00<s>$42.00</s></div></div>
<div class="photo" role="img" aria-label="Bowl of dark chocolate pieces" style="left:40px;top:1887px;width:112px;height:112px;background:radial-gradient(circle,#3a2a22 0%,#5a4436 50%,#e6e6e6 75%)"></div>
<div class="abs" style="left:173px;top:1885px"><div>Product 01</div><div class="stars" style="margin-top:4px">★★★★★<em>6 Review(s)</em></div><div class="price">$36.00<s>$42.00</s></div></div>
<div class="photo" role="img" aria-label="Pastel macarons with a cup" style="left:417px;top:1887px;width:112px;height:112px;background:linear-gradient(135deg,#f0ece2,#d8c6a4 45%,#b8c8a8 70%,#f0ece2)"></div>
<div class="abs" style="left:552px;top:1885px"><div>Product 01</div><div class="stars" style="margin-top:4px">★★★★★<em>6 Review(s)</em></div><div class="price">$36.00<s>$42.00</s></div></div>

<!-- testimonial -->
<h2 class="abs sec-title" style="left:796px;top:1654px">Testimonial</h2>
<div class="abs" style="left:795px;top:1746px;width:80px;height:80px;border-radius:50%;background:var(--sand)"></div>
<div class="abs" style="left:898px;top:1770px;font-size:12px;line-height:16px">John Doe<br><i style="color:var(--muted)">Parent</i></div>
<div class="abs" style="left:795px;top:1842px;font-size:28px;font-family:Georgia,serif;font-weight:700">“</div>
<p class="abs quote" style="left:795px;top:1888px">Lorem Ipsum is simply dummy text of the printing and typesetting industry. Lorem Ipsum has been then industry's standard dummy text ever since the 1500s. Blah blah blah blah.</p>
<div class="abs" style="left:795px;top:1993px;display:flex;gap:6px"><i style="width:9px;height:9px;border-radius:50%;background:var(--blue)"></i><i style="width:9px;height:9px;border-radius:50%;background:#ccd"></i><i style="width:9px;height:9px;border-radius:50%;background:#ccd"></i></div>

<!-- blogs -->
<h2 class="abs sec-title" style="left:40px;top:2072px">Blogs</h2>
<div class="abs" role="img" aria-label="Blog cover photo" style="left:40px;top:2160px;width:239px;height:180px;background:#dcdcdc"></div>
<article class="abs blog" style="left:291px;top:2178px">
  <h3>New stories</h3>
  <div class="meta"><span><i class="avatar"></i>John Doe</span><span>▦ April 25, 2019</span></div>
  <p>We held a very successful kids party and it was much fun...</p>
  <div class="stats"><span>● 123 Comments</span><span>▲ 98 likes</span></div>
</article>
<div class="abs" role="img" aria-label="Blog cover photo" style="left:606px;top:2160px;width:239px;height:180px;background:#dcdcdc"></div>
<article class="abs blog" style="left:860px;top:2178px">
  <h3>New kids products trends</h3>
  <div class="meta"><span><i class="avatar"></i>John Doe</span><span>▦ April 25, 2019</span></div>
  <p>We held a very successful kids party and it was much fun...</p>
  <div class="stats"><span>● 123 Comments</span><span>▲ 98 likes</span></div>
</article>

<!-- newsletter -->
<div class="photo" role="img" aria-label="Two kids wearing red and blue superhero masks" style="left:108px;top:2430px;width:452px;height:260px;background:linear-gradient(100deg,#e8a030 0%,#d23a2a 35%,#e06040 55%,#4a8ac8 75%,#f2c24a 100%)"></div>
<h2 class="abs" style="left:608px;top:2458px;font-size:36px;font-weight:600">Newsletter</h2>
<p class="abs" style="left:609px;top:2534px;width:520px;font-size:13px;font-style:italic;line-height:18px">Subscribe to the Plumwicks shop list to receive updates on new arrivals, special offers and other discount information</p>
<div class="abs subscribe">Enter your email<b>Subscribe</b></div>

<!-- footer -->
<footer class="abs footer">
  <div class="abs" style="left:63px;top:70px;width:190px;height:190px;border-radius:50%;background:#fff;border:6px solid var(--blue);display:flex;align-items:center;justify-content:center;text-align:center"><span class="brand" style="font-size:30px">Plumwicks<br>Shop</span></div>
  <div class="abs small" style="left:66px;top:290px">Terms Of Use</div>
  <div class="abs small" style="left:66px;top:327px">Shipping and Returns</div>

  <h3 style="left:342px">FOLLOW US</h3>
  <div class="abs" style="left:342px;top:148px">
    <div class="social"><i></i>Plumwicks</div>
    <div class="social"><i class="c"></i>Plumwicks</div>
    <div class="social"><i></i>Plumwicks</div>
    <div class="social"><i></i>Plumwicks</div>
  </div>

  <h3 style="left:567px">CONTACT</h3>
  <div class="abs" style="left:567px;top:140px;width:240px">
    <div class="cline"><span>⌖</span><span>Address:<br>Blah blah blah blah blah #100:<br>Soouth Ciunty, Blah, Blah</span></div>
    <div style="border-top:1px solid #45475a;margin:18px 0 26px"></div>
    <div class="cline" style="margin-bottom:12px"><span>☏</span>Phone: (555) 010-3333</div>
    <div class="cline" style="margin-bottom:12px"><span>▤</span>Fax: (555) 010-4444</div>
    <div class="cline" style="margin-bottom:12px"><span>✉</span>Email: <a>info@plumwicksshop.com</a></div>
    <div class="cline"><span>◍</span>Website: <a>www.plumwicksshop.com</a></div>
  </div>

  <h3 style="left:899px">NEWSLETTER</h3>
  <p class="abs small" style="left:900px;top:138px;width:250px;line-height:16px">Subscribe to our Newsletter for thelatest updates, events, services and products.</p>
  <div class="abs f-input" style="left:900px;top:200px">Your Email</div>
  <div class="abs f-btn" style="left:900px;top:246px">Subscribe</div>
</footer>

</body>
</html>
```